Tallgrove Vale Management

I need a professional website. My current website is tallgrovevalemanagement.com and I hate it. It was created with some AI tool very quickly because I needed a site up and running with no advanced notice. I’m open to all designs .. I trust you, the professionals will deliver the results I’m anxiously awaiting! :)

```html
<!DOCTYPE html>
<html lang="en">
<head>
<meta charset="utf-8">
<title>Tallgrove Vale Management</title>
<link href="https://fonts.googleapis.com/css2?family=Plus+Jakarta+Sans:wght@500;600;700;800&family=Inter:wght@400;500;600;700&display=swap" rel="stylesheet">
<style>
:root{
  --navy:#1f3461;
  --navy-dark:#172a52;
  --red:#d3282f;
  --ink:#1c2640;
  --muted:#6b7488;
  --line:#e6e8ee;
  --soft:#f4f5f8;
  --white:#ffffff;
  --footer:#1b1c22;
}
*{margin:0;padding:0;box-sizing:border-box}
html,body{width:1200px;height:5245px;overflow:hidden}
body{font-family:"Inter",sans-serif;color:var(--ink);background:var(--white);position:relative}
h1,h2,h3,.display{font-family:"Plus Jakarta Sans",sans-serif}
.wrap{width:744px;margin:0 auto;position:relative}
.eyebrow{font-size:8px;font-weight:700;letter-spacing:1.2px;color:var(--red);text-transform:uppercase}
.btn{display:inline-flex;align-items:center;gap:6px;font-size:10px;font-weight:600;padding:0 16px;height:32px;border-radius:4px;text-decoration:none}
.btn-navy{background:var(--navy);color:#fff}
.btn-red{background:var(--red);color:#fff}
.btn-outline{border:1.5px solid var(--navy);color:var(--navy);background:#fff}
.arrow{width:9px;height:9px}

/* nav */
.nav{position:absolute;top:0;left:0;width:1200px;height:50px;background:rgba(255,255,255,.95);z-index:5}
.nav-links{position:absolute;left:230px;top:19px;display:flex;gap:14px;font-size:10px;font-weight:500}
.nav-links a{color:var(--ink);text-decoration:none}
.brand{position:absolute;left:50%;top:10px;transform:translateX(-50%);display:flex;align-items:center;gap:6px;background:#fff;padding:10px 12px;border-radius:6px}
.brand-mark{width:14px;height:14px;background:var(--red)}
.brand-name{font-family:"Plus Jakarta Sans",sans-serif;font-weight:800;font-size:13px;color:var(--navy);letter-spacing:.5px}
.nav .btn{position:absolute;right:230px;top:9px;height:32px}

/* hero */
.hero{position:absolute;top:0;left:0;width:1200px;height:740px}
.hero-photo{position:absolute;inset:0;background:linear-gradient(180deg,#a9c6e6 0%,#cfdceb 18%,#7f8b76 32%,#4f6b3a 50%,#3e5a2e 70%,#5d6b4a 100%)}
.hero-shape{position:absolute;inset:0}
.intro{position:absolute;top:790px;left:0;width:1200px;text-align:center}
.intro h1{font-size:36px;line-height:42px;font-weight:700;color:var(--navy);letter-spacing:-.5px}
.intro h1 .hl{color:var(--red)}
.intro p{width:600px;margin:18px auto 0;font-size:11px;line-height:19px;color:var(--muted)}
.intro .actions{margin-top:20px;display:flex;justify-content:center;gap:10px}

/* about */
.about{position:absolute;top:1065px;left:228px;width:744px;height:355px}
.about-photo{position:absolute;left:0;top:0;width:354px;height:355px;border-radius:10px;background:linear-gradient(135deg,#d9cbb5 0%,#b8a284 40%,#6f6a63 75%,#8a9aa8 100%)}
.about-stat{position:absolute;left:216px;top:270px;width:138px;height:85px;background:var(--navy);border-radius:8px 0 10px 0;color:#fff;padding:14px 14px}
.about-stat strong{font-family:"Plus Jakarta Sans",sans-serif;font-size:22px;font-weight:700;display:block}
.about-stat span{font-size:8px;line-height:11px;display:block;margin-top:4px;opacity:.85}
.about-copy{position:absolute;left:390px;top:20px;width:354px}
.about-copy h2{font-size:28px;line-height:31px;color:var(--navy);margin-top:10px;font-weight:700;letter-spacing:-.3px}
.about-copy p{font-size:9.5px;line-height:16px;color:var(--muted);margin-top:14px}
.checks{display:grid;grid-template-columns:1fr 1fr;gap:18px 0;margin-top:18px}
.check{display:flex;align-items:center;gap:8px;font-size:8.5px;font-weight:600;color:var(--navy)}
.check i{width:18px;height:18px;background:var(--navy);border-radius:4px;display:flex;align-items:center;justify-content:center}

/* why */
.why{position:absolute;top:1510px;left:0;width:1200px;height:630px;background:var(--navy);color:#fff}
.why .wrap{padding-top:85px}
.why h2{font-size:28px;line-height:36px;font-weight:700;margin-top:8px}
.why .lead{font-size:9.5px;line-height:16px;width:430px;opacity:.75;margin-top:10px}
.why-grid{display:grid;grid-template-columns:repeat(3,1fr);gap:14px 12px;margin-top:40px}
.why-card{height:145px;background:rgba(255,255,255,.06);border:1px solid rgba(255,255,255,.12);border-radius:8px;padding:20px 18px}
.icon-red{width:28px;height:28px;background:var(--red);border-radius:5px;display:flex;align-items:center;justify-content:center}
.why-card h3{font-size:11px;font-weight:700;margin-top:26px}
.why-card p{font-size:8px;line-height:13px;opacity:.6;margin-top:6px}

/* services */
.services{position:absolute;top:2140px;left:0;width:1200px;height:605px}
.section-head{text-align:center}
.section-head h2{font-size:28px;line-height:36px;font-weight:700;color:var(--navy);margin-top:8px}
.section-head p{width:420px;margin:8px auto 0;font-size:9.5px;line-height:16px;color:var(--muted)}
.services .section-head{padding-top:80px}
.plans{position:absolute;top:245px;left:228px;width:744px;height:300px}
.plan{position:absolute;top:0;width:170px;height:290px;background:#fff;border:1px solid var(--line);border-radius:8px;padding:20px 18px}
.plan .eyebrow{font-size:7.5px}
.price{font-family:"Plus Jakarta Sans",sans-serif;font-size:28px;font-weight:700;color:var(--navy);margin-top:10px}
.price small{font-size:8px;font-weight:500;color:var(--muted)}
.plan p{font-size:8px;line-height:12px;color:var(--muted);margin-top:6px;height:48px}
.plan ul{list-style:none;margin-top:8px}
.plan li{font-size:8px;line-height:12px;color:var(--ink);display:flex;gap:6px;margin-bottom:8px}
.plan li svg{flex:none;margin-top:2px}
.plan .btn{position:absolute;left:18px;right:18px;bottom:18px;height:28px;justify-content:center;font-size:8.5px}
.plan-featured{top:-16px!important;height:312px!important;background:var(--navy)!important;border:none!important;color:#fff;box-shadow:0 14px 30px rgba(31,52,97,.35);width:194px!important}
.plan-featured .eyebrow{color:#fff;opacity:.8}
.plan-featured .price{color:#fff}
.plan-featured .price small,.plan-featured p{color:rgba(255,255,255,.7)}
.plan-featured li{color:#fff}
.badge{position:absolute;top:-8px;left:50%;transform:translateX(-50%);background:var(--red);color:#fff;font-size:7px;font-weight:700;padding:4px 10px;border-radius:3px;letter-spacing:.5px;white-space:nowrap}

/* process */
.process{position:absolute;top:2745px;left:0;width:1200px;height:455px;background:var(--soft)}
.process .section-head{padding-top:80px}
.steps{display:grid;grid-template-columns:repeat(4,1fr);gap:12px;width:744px;margin:48px auto 0}
.step{height:168px;background:#fff;border:1px solid var(--line);border-radius:8px;padding:20px 16px;position:relative}
.step .num{position:absolute;right:16px;top:18px;font-family:"Plus Jakarta Sans",sans-serif;font-size:30px;font-weight:700;color:#eceef3}
.icon-navy{width:36px;height:36px;background:var(--navy);border-radius:7px;display:flex;align-items:center;justify-content:center}
.step h3{font-size:10.5px;font-weight:700;color:var(--navy);margin-top:20px}
.step p{font-size:8px;line-height:13px;color:var(--muted);margin-top:6px}

/* results */
.results{position:absolute;top:3200px;left:0;width:1200px;height:325px;background:var(--navy)}
.results .section-head{padding-top:60px}
.results h2{color:#fff}
.stats{display:grid;grid-template-columns:repeat(4,1fr);gap:14px;width:744px;margin:26px auto 0}
.stat{height:86px;background:#fff;border-radius:6px;text-align:center;padding-top:14px}
.stat strong{font-family:"Plus Jakarta Sans",sans-serif;font-size:36px;font-weight:700;color:var(--red);display:block;line-height:40px}
.stat span{font-size:7.5px;letter-spacing:.8px;color:var(--muted);text-transform:uppercase}

/* testimonials */
.testimonials{position:absolute;top:3525px;left:0;width:1200px;height:400px}
.testimonials .section-head{padding-top:70px}
.quotes{display:grid;grid-template-columns:repeat(3,1fr);gap:16px;width:744px;margin:28px auto 0}
.quote{height:180px;background:#fff;border:1px solid var(--line);border-radius:8px;padding:22px 18px;box-shadow:0 6px 18px rgba(20,30,60,.05)}
.stars{color:var(--red);font-size:11px;letter-spacing:2px}
.quote p{font-size:9px;line-height:15px;color:var(--ink);margin-top:14px;padding-bottom:14px;border-bottom:1px solid var(--line)}
.quote cite{display:block;font-style:normal;font-size:8px;font-weight:600;color:var(--navy);margin-top:10px}

/* cta */
.cta{position:absolute;top:3925px;left:0;width:1200px;height:335px;background:linear-gradient(100deg,#2a3d66 0%,#1f3461 45%,#243a69 100%);color:#fff;text-align:center}
.cta h2{font-size:28px;line-height:36px;font-weight:700;padding-top:80px}
.cta p{width:560px;margin:10px auto 0;font-size:9.5px;line-height:16px;opacity:.75}
.cta .btn{margin-top:26px;height:34px}

/* contact */
.contact{position:absolute;top:4260px;left:228px;width:744px;height:510px}
.contact-copy{position:absolute;left:0;top:70px;width:330px}
.contact-copy h2{font-size:28px;line-height:33px;font-weight:700;color:var(--navy);margin-top:8px}
.contact-copy p{font-size:9.5px;line-height:16px;color:var(--muted);margin-top:14px}
.info{display:flex;align-items:center;gap:10px;margin-top:14px}
.info i{width:28px;height:28px;background:var(--navy);border-radius:5px;display:flex;align-items:center;justify-content:center}
.info small{display:block;font-size:6.5px;letter-spacing:.6px;color:var(--muted);text-transform:uppercase}
.info span{font-size:9.5px;font-weight:600;color:var(--navy)}
.form{position:absolute;left:390px;top:50px;width:354px;height:400px;background:#fff;border:1px solid var(--line);border-radius:8px;padding:26px 24px;box-shadow:0 6px 18px rgba(20,30,60,.05)}
.form-grid{display:grid;grid-template-columns:1fr 1fr;gap:16px 14px}
.field label{display:block;font-size:8px;font-weight:600;color:var(--navy);margin-bottom:6px}
.field .input{height:30px;border:1px solid var(--line);border-radius:4px;background:#fafbfc;font-size:8.5px;color:var(--muted);padding:9px 10px}
.field-full{margin-top:16px}
.field-full .input{height:98px}
.form .btn{width:100%;justify-content:center;margin-top:20px;height:32px}

/* footer */
.footer{position:absolute;top:4770px;left:0;width:1200px;height:475px}
.footer svg.bands{position:absolute;inset:0}
.footer-inner{position:absolute;left:0;width:1200px;top:190px;text-align:center;color:#fff}
.footer .brand-f{display:inline-flex;align-items:center;gap:6px}
.footer .brand-f .brand-mark{width:16px;height:16px}
.footer .brand-f .brand-name{color:#fff;font-size:16px}
.footer p{width:440px;margin:26px auto 0;font-size:9.5px;line-height:16px;opacity:.75}
.footer-links{display:flex;justify-content:center;gap:14px;margin-top:20px;font-size:8.5px}
.socials{display:flex;justify-content:center;gap:10px;margin-top:16px}
.socials span{width:22px;height:22px;border-radius:50%;border:1px solid rgba(255,255,255,.3)}
.copyright{position:absolute;left:0;width:1200px;bottom:22px;text-align:center;font-size:8px;color:rgba(255,255,255,.5)}
</style>
</head>
<body>

<header class="nav">
  <nav class="nav-links"><a href="#">Home</a><a href="#">About</a><a href="#">Services</a><a href="#">Process</a><a href="#">Contact</a></nav>
  <div class="brand"><span class="brand-mark"></span><span class="brand-name">TALLGROVE</span></div>
  <a class="btn btn-red" href="#">Get Started <svg class="arrow" viewBox="0 0 10 10"><path d="M1 5h7M5 2l3 3-3 3" stroke="#fff" stroke-width="1.4" fill="none"/></svg></a>
</header>

<section class="hero">
  <div class="hero-photo" role="img" aria-label="Aerial view of a suburban neighborhood with a city skyline behind"></div>
  <svg class="hero-shape" viewBox="0 0 1200 740" preserveAspectRatio="none">
    <polygon points="0,440 600,630 1200,440 1200,740 0,740" fill="#d3282f"/>
    <polygon points="0,495 600,680 1200,495 1200,740 0,740" fill="#1f3461"/>
    <polygon points="0,560 600,740 1200,560 1200,740 0,740" fill="#ffffff"/>
  </svg>
</section>

<section class="intro">
  <h1>Property Management Built on<br><span class="hl">Trust, Strategy</span> &amp; Results.</h1>
  <p>Tallgrove Vale Management partners with property owners to maximize asset performance, simplify operations, and create exceptional tenant experiences. Through proactive management, data-driven strategies, and transparent communication, we protect your investment while delivering long-term value.</p>
  <div class="actions">
    <a class="btn btn-navy" href="#">Get Started <svg class="arrow" viewBox="0 0 10 10"><path d="M1 5h7M5 2l3 3-3 3" stroke="#fff" stroke-width="1.4" fill="none"/></svg></a>
    <a class="btn btn-outline" href="#">Explore Services</a>
  </div>
</section>

<section class="about">
  <div class="about-photo" role="img" aria-label="Property manager standing in front of modern apartment buildings"></div>
  <div class="about-stat"><strong>20+</strong><span>Years serving Ohio<br>property owners</span></div>
  <div class="about-copy">
    <div class="eyebrow">About Tallgrove</div>
    <h2>Your Trusted Partner in Property Management</h2>
    <p>At Tallgrove Vale Management, we believe successful property management begins with strong partnerships. Our team combines decades of industry expertise with modern technology to deliver comprehensive solutions that improve operational efficiency, protect investments, and enhance tenant satisfaction.</p>
    <p>From regulatory compliance and financial oversight to preventative maintenance and transparent reporting, every decision is guided by one objective—helping your property perform at its highest potential.</p>
    <div class="checks">
      <div class="check"><i><svg width="9" height="9" viewBox="0 0 10 10"><path d="M2 5l2 2 4-4" stroke="#fff" stroke-width="1.5" fill="none"/></svg></i>Strategic Planning</div>
      <div class="check"><i><svg width="9" height="9" viewBox="0 0 10 10"><path d="M2 5l2 2 4-4" stroke="#fff" stroke-width="1.5" fill="none"/></svg></i>Preventive Maintenance</div>
      <div class="check"><i><svg width="9" height="9" viewBox="0 0 10 10"><path d="M2 5l2 2 4-4" stroke="#fff" stroke-width="1.5" fill="none"/></svg></i>Financial Reporting</div>
      <div class="check"><i><svg width="9" height="9" viewBox="0 0 10 10"><path d="M2 5l2 2 4-4" stroke="#fff" stroke-width="1.5" fill="none"/></svg></i>Tenant Relations</div>
    </div>
  </div>
</section>

<section class="why">
  <div class="wrap">
    <div class="eyebrow">Why Tallgrove</div>
    <h2>Why Property Owners<br>Choose Tallgrove</h2>
    <p class="lead">Our commitment goes beyond managing properties—we build long-term partnerships focused on protecting your investment, improving operational performance, and creating lasting value.</p>
    <div class="why-grid">
      <div class="why-card"><div class="icon-red"><svg width="14" height="14" viewBox="0 0 14 14"><path d="M2 2v10h10M4 9l3-3 2 2 3-4" stroke="#fff" stroke-width="1.3" fill="none"/></svg></div><h3>Strategic Asset Management</h3><p>We develop customized management strategies designed to maximize long-term property value.</p></div>
      <div class="why-card"><div class="icon-red"><svg width="14" height="14" viewBox="0 0 14 14"><path d="M2 3h10v7H6l-3 2v-2H2z" stroke="#fff" stroke-width="1.3" fill="none"/></svg></div><h3>Transparent Communication</h3><p>Receive consistent updates, detailed reporting, and responsive support whenever you need it.</p></div>
      <div class="why-card"><div class="icon-red"><svg width="14" height="14" viewBox="0 0 14 14"><path d="M7 1.5l4.5 2v3.5c0 3-2 4.8-4.5 5.5C4.5 11.8 2.5 10 2.5 7V3.5z" stroke="#fff" stroke-width="1.3" fill="none"/></svg></div><h3>Regulatory Compliance</h3><p>Stay ahead of changing regulations with expert guidance and proactive compliance management.</p></div>
      <div class="why-card"><div class="icon-red"><svg width="14" height="14" viewBox="0 0 14 14"><path d="M3 11l5-5M9 2a3 3 0 0 0 3 3L9 8 6 5z" stroke="#fff" stroke-width="1.3" fill="none"/></svg></div><h3>Preventive Maintenance</h3><p>Reduce unexpected costs through scheduled inspections and maintenance planning.</p></div>
      <div class="why-card"><div class="icon-red"><svg width="14" height="14" viewBox="0 0 14 14"><path d="M2 12h10M4 10V6M7 10V3M10 10V7" stroke="#fff" stroke-width="1.4" fill="none"/></svg></div><h3>Data-Driven Decisions</h3><p>Advanced reporting and analytics provide actionable insights that improve performance.</p></div>
      <div class="why-card"><div class="icon-red"><svg width="14" height="14" viewBox="0 0 14 14"><circle cx="5" cy="5" r="2" stroke="#fff" stroke-width="1.3" fill="none"/><circle cx="10" cy="5" r="2" stroke="#fff" stroke-width="1.3" fill="none"/><path d="M1.5 12c0-2 1.5-3.5 3.5-3.5S8.5 10 8.5 12M8 9c.6-.4 1.3-.5 2-.5 2 0 3 1.5 3 3.5" stroke="#fff" stroke-width="1.3" fill="none"/></svg></div><h3>Dedicated Partnership</h3><p>We operate as an extension of your team—not simply another service provider.</p></div>
    </div>
  </div>
</section>

<section class="services">
  <div class="section-head">
    <div class="eyebrow">Services</div>
    <h2>Strategic Property<br>Management Solutions</h2>
    <p>Our flexible management packages are designed to meet the unique needs of every property owner—from individual investments to large-scale portfolios.</p>
  </div>
  <div class="plans">
    <div class="plan" style="left:0">
      <div class="eyebrow">Basic Service</div>
      <div class="price">$99 <small>/mo</small></div>
      <p>Perfect for individual property owners seeking dependable day-to-day management.</p>
      <ul>
        <li><svg width="8" height="8" viewBox="0 0 10 10"><path d="M1.5 5l2.5 2.5 4.5-5" stroke="#1f3461" stroke-width="1.5" fill="none"/></svg>Property Oversight</li>
        <li><svg width="8" height="8" viewBox="0 0 10 10"><path d="M1.5 5l2.5 2.5 4.5-5" stroke="#1f3461" stroke-width="1.5" fill="none"/></svg>Tenant Communication</li>
        <li><svg width="8" height="8" viewBox="0 0 10 10"><path d="M1.5 5l2.5 2.5 4.5-5" stroke="#1f3461" stroke-width="1.5" fill="none"/></svg>Monthly Reports</li>
        <li><svg width="8" height="8" viewBox="0 0 10 10"><path d="M1.5 5l2.5 2.5 4.5-5" stroke="#1f3461" stroke-width="1.5" fill="none"/></svg>Basic Maintenance Coordination</li>
      </ul>
      <a class="btn btn-navy" href="#">Choose Plan <svg class="arrow" viewBox="0 0 10 10"><path d="M1 5h7M5 2l3 3-3 3" stroke="#fff" stroke-width="1.4" fill="none"/></svg></a>
    </div>
    <div class="plan" style="left:183px">
      <div class="eyebrow">Intermediate Service</div>
      <div class="price">$149 <small>/mo</small></div>
      <p>Ideal for growing property portfolios requiring enhanced operational support.</p>
      <ul>
        <li><svg width="8" height="8" viewBox="0 0 10 10"><path d="M1.5 5l2.5 2.5 4.5-5" stroke="#1f3461" stroke-width="1.5" fill="none"/></svg>Everything in Basic</li>
        <li><svg width="8" height="8" viewBox="0 0 10 10"><path d="M1.5 5l2.5 2.5 4.5-5" stroke="#1f3461" stroke-width="1.5" fill="none"/></svg>Vendor Coordination</li>
        <li><svg width="8" height="8" viewBox="0 0 10 10"><path d="M1.5 5l2.5 2.5 4.5-5" stroke="#1f3461" stroke-width="1.5" fill="none"/></svg>Preventive Maintenance</li>
        <li><svg width="8" height="8" viewBox="0 0 10 10"><path d="M1.5 5l2.5 2.5 4.5-5" stroke="#1f3461" stroke-width="1.5" fill="none"/></svg>Financial Tracking</li>
      </ul>
      <a class="btn btn-navy" href="#">Choose Plan <svg class="arrow" viewBox="0 0 10 10"><path d="M1 5h7M5 2l3 3-3 3" stroke="#fff" stroke-width="1.4" fill="none"/></svg></a>
    </div>
    <div class="plan plan-featured" style="left:366px">
      <span class="badge">MOST POPULAR</span>
      <div class="eyebrow">Advanced Service</div>
      <div class="price">$199 <small>/mo</small></div>
      <p>Designed for owners seeking comprehensive management and optimization.</p>
      <ul>
        <li><svg width="8" height="8" viewBox="0 0 10 10"><path d="M1.5 5l2.5 2.5 4.5-5" stroke="#d3282f" stroke-width="1.5" fill="none"/></svg>Everything Included</li>
        <li><svg width="8" height="8" viewBox="0 0 10 10"><path d="M1.5 5l2.5 2.5 4.5-5" stroke="#d3282f" stroke-width="1.5" fill="none"/></svg>Compliance Management</li>
        <li><svg width="8" height="8" viewBox="0 0 10 10"><path d="M1.5 5l2.5 2.5 4.5-5" stroke="#d3282f" stroke-width="1.5" fill="none"/></svg>Performance Reporting</li>
        <li><svg width="8" height="8" viewBox="0 0 10 10"><path d="M1.5 5l2.5 2.5 4.5-5" stroke="#d3282f" stroke-width="1.5" fill="none"/></svg>Asset Optimization</li>
      </ul>
      <a class="btn btn-red" href="#">Choose Plan <svg class="arrow" viewBox="0 0 10 10"><path d="M1 5h7M5 2l3 3-3 3" stroke="#fff" stroke-width="1.4" fill="none"/></svg></a>
    </div>
    <div class="plan" style="left:574px">
      <div class="eyebrow">Advanced+ Service</div>
      <div class="price">$249 <small>/mo</small></div>
      <p>Enterprise-level property management with strategic consulting and priority support.</p>
      <ul>
        <li><svg width="8" height="8" viewBox="0 0 10 10"><path d="M1.5 5l2.5 2.5 4.5-5" stroke="#1f3461" stroke-width="1.5" fill="none"/></svg>Dedicated Property Manager</li>
        <li><svg width="8" height="8" viewBox="0 0 10 10"><path d="M1.5 5l2.5 2.5 4.5-5" stroke="#1f3461" stroke-width="1.5" fill="none"/></svg>Advanced Analytics</li>
        <li><svg width="8" height="8" viewBox="0 0 10 10"><path d="M1.5 5l2.5 2.5 4.5-5" stroke="#1f3461" stroke-width="1.5" fill="none"/></svg>Portfolio Consulting</li>
        <li><svg width="8" height="8" viewBox="0 0 10 10"><path d="M1.5 5l2.5 2.5 4.5-5" stroke="#1f3461" stroke-width="1.5" fill="none"/></svg>Priority Support</li>
      </ul>
      <a class="btn btn-navy" href="#">Choose Plan <svg class="arrow" viewBox="0 0 10 10"><path d="M1 5h7M5 2l3 3-3 3" stroke="#fff" stroke-width="1.4" fill="none"/></svg></a>
    </div>
  </div>
</section>

<section class="process">
  <div class="section-head">
    <div class="eyebrow">Our Process</div>
    <h2>Our Proven Management<br>Process</h2>
  </div>
  <div class="steps">
    <div class="step"><span class="num">01</span><div class="icon-navy"><svg width="16" height="16" viewBox="0 0 16 16"><rect x="3.5" y="3" width="9" height="11" rx="1" stroke="#fff" stroke-width="1.3" fill="none"/><path d="M6 2h4v2H6zM6 8h4M6 11h4" stroke="#fff" stroke-width="1.3" fill="none"/></svg></div><h3>Property Assessment</h3><p>We evaluate your property, operational needs, and investment goals.</p></div>
    <div class="step"><span class="num">02</span><div class="icon-navy"><svg width="16" height="16" viewBox="0 0 16 16"><circle cx="8" cy="8" r="5.5" stroke="#fff" stroke-width="1.3" fill="none"/><path d="M10 6L7 7 6 10l3-1z" stroke="#fff" stroke-width="1.2" fill="none"/></svg></div><h3>Strategic Planning</h3><p>A customized management plan is developed to maximize efficiency and value.</p></div>
    <div class="step"><span class="num">03</span><div class="icon-navy"><svg width="16" height="16" viewBox="0 0 16 16"><circle cx="8" cy="8" r="2.2" stroke="#fff" stroke-width="1.3" fill="none"/><circle cx="8" cy="8" r="5" stroke="#fff" stroke-width="1.3" fill="none" stroke-dasharray="2 1.6"/></svg></div><h3>Implementation</h3><p>Our specialists oversee maintenance, tenant relations, compliance, and financial operations.</p></div>
    <div class="step"><span class="num">04</span><div class="icon-navy"><svg width="16" height="16" viewBox="0 0 16 16"><path d="M2.5 12l4-4 2.5 2.5 4.5-5M10 5.5h3.5V9" stroke="#fff" stroke-width="1.3" fill="none"/></svg></div><h3>Continuous Optimization</h3><p>Through ongoing reporting and analysis, we continuously improve property performance.</p></div>
  </div>
</section>

<section class="results">
  <div class="section-head">
    <div class="eyebrow">Performance</div>
    <h2>Delivering Measurable<br>Results</h2>
  </div>
  <div class="stats">
    <div class="stat"><strong>500+</strong><span>Managed Properties</span></div>
    <div class="stat"><strong>98%</strong><span>Client Satisfaction</span></div>
    <div class="stat"><strong>20+</strong><span>Years Experience</span></div>
    <div class="stat"><strong>95%</strong><span>Average Occupancy</span></div>
  </div>
</section>

<section class="testimonials">
  <div class="section-head">
    <div class="eyebrow">Testimonials</div>
    <h2>Trusted by Property Owners</h2>
  </div>
  <div class="quotes">
    <div class="quote"><div class="stars">★★★★★</div><p>"Tallgrove Vale Management transformed the way we manage our investment properties. Their professionalism, communication, and attention to detail have exceeded every expectation."</p><cite>— Residential Investor</cite></div>
    <div class="quote"><div class="stars">★★★★★</div><p>"Their proactive maintenance and financial reporting have helped us reduce operational costs while improving tenant satisfaction."</p><cite>— Commercial Property Owner</cite></div>
    <div class="quote"><div class="stars">★★★★★</div><p>"They truly operate as a partner rather than simply another management company."</p><cite>— Portfolio Investor</cite></div>
  </div>
</section>

<section class="cta" role="img" aria-label="Business professionals in an office, overlaid with navy tone">
  <h2>Ready to Maximize Your<br>Property’s Potential?</h2>
  <p>Partner with Tallgrove Vale Management and experience professional property management focused on protecting your investment, increasing operational efficiency, and creating long- term value.</p>
  <a class="btn btn-red" href="#">Schedule Consultation <svg class="arrow" viewBox="0 0 10 10"><path d="M1 5h7M5 2l3 3-3 3" stroke="#fff" stroke-width="1.4" fill="none"/></svg></a>
</section>

<section class="contact">
  <div class="contact-copy">
    <div class="eyebrow">Contact</div>
    <h2>Submit Your Property Management Inquiry</h2>
    <p>Complete the inquiry form to schedule an initial consultation with our experienced team. We’ll discuss your goals, evaluate your property’s needs, and demonstrate how our management solutions can improve operational performance and tenant satisfaction.</p>
    <div class="info" style="margin-top:24px"><i><svg width="12" height="12" viewBox="0 0 12 12"><rect x="1.5" y="2.5" width="9" height="7" rx="1" stroke="#fff" stroke-width="1.2" fill="none"/><path d="M1.5 3.5L6 7l4.5-3.5" stroke="#fff" stroke-width="1.2" fill="none"/></svg></i><div><small>Email</small><span>info@tallgrovevalemanagement.com</span></div></div>
    <div class="info"><i><svg width="12" height="12" viewBox="0 0 12 12"><path d="M3 1.5l1.8 2.2-1 1.3a6 6 0 0 0 3.2 3.2l1.3-1L10.5 9 9.5 10.5C5 10.5 1.5 7 1.5 2.5z" stroke="#fff" stroke-width="1.1" fill="none"/></svg></i><div><small>Phone</small><span>(123) 456-7890</span></div></div>
    <div class="info"><i><svg width="12" height="12" viewBox="0 0 12 12"><path d="M6 11s3.5-3.5 3.5-6a3.5 3.5 0 0 0-7 0C2.5 7.5 6 11 6 11z" stroke="#fff" stroke-width="1.2" fill="none"/><circle cx="6" cy="5" r="1.2" fill="#fff"/></svg></i><div><small>Location</small><span>Ohio, United States</span></div></div>
  </div>
  <div class="form">
    <div class="form-grid">
      <div class="field"><label>Full Name</label><div class="input"></div></div>
      <div class="field"><label>Email Address</label><div class="input"></div></div>
      <div class="field"><label>Phone Number</label><div class="input"></div></div>
      <div class="field"><label>Property Type</label><div class="input">Select type</div></div>
    </div>
    <div class="field field-full"><label>Message</label><div class="input"></div></div>
    <a class="btn btn-navy" href="#">Submit Inquiry <svg class="arrow" viewBox="0 0 10 10"><path d="M1 5h7M5 2l3 3-3 3" stroke="#fff" stroke-width="1.4" fill="none"/></svg></a>
  </div>
</section>

<footer class="footer">
  <svg class="bands" viewBox="0 0 1200 475" preserveAspectRatio="none">
    <polygon points="0,165 600,0 1200,165 1200,475 0,475" fill="#1f3461"/>
    <polygon points="0,270 600,120 1200,270 1200,475 0,475" fill="#d3282f"/>
    <polygon points="0,305 600,150 1200,305 1200,475 0,475" fill="#1f3461"/>
    <polygon points="0,330 600,220 1200,330 1200,475 0,475" fill="#1b1c22"/>
    <rect x="0" y="330" width="1200" height="145" fill="#1b1c22"/>
  </svg>
  <div class="footer-inner">
    <div class="brand-f"><span class="brand-mark"></span><span class="brand-name">TALLGROVE</span></div>
    <p>Property management built on trust, strategy, and results. Serving Ohio property owners with proactive, data-driven management since day one.</p>
    <div class="footer-links"><span>Home</span><span>About</span><span>Services</span><span>Process</span><span>Contact</span></div>
    <div class="socials"><span></span><span></span><span></span></div>
  </div>
  <div class="copyright">© 2025 Tallgrove Vale Management LLC. All Rights Reserved.</div>
</footer>

</body>
</html>
```